Car rental website design for a UAE car rental company

This project is about creating a new website design for a car rental company located in Dubai (United Arab Emirates), I opened the same project a few months ago but I didn't receive a lot of appealing entries so I closed it but this time I am marking the project as guaranteed to avoid such situation again, if you have already provided a design before then please re-submit again on this project so that it is considered while reviewing all the designs

A few important things:

1- We need a simple non-complex design
2- The final deliverable would be 2 screens (PSD, JPEG ... etc), the first screen is for the home page and the second screen is for an internal page
3- The home page must have a section that end users can use to rent a car online directly from the home page instead of going into some inner pages
4- The current website is very old and not very appealing so avoid creating a similar design (www.quarvin-drive.example)
5- The name is Quarvin but the company rents normal cars (no Limousin cars will be rented) so avoid adding any fancy cars in the images/graphics used in the design, just normal end users cars
6- The expected pages would be: home, About us, Our team, Strategy, Contact us and links to social media pages
7- The attachments include the company's logo and some screens from other car rental companies that provide online rentals/payments

If you have any questions please feel free to ask and please note that we will need the designs urgently

Thanks

Target Market(s)

Dubai - United Arab Emirates

Industry/Entity Type

It Company

Number of Pages Required

2 page

Font styles to use
Sans Serif

Requirements
Must have
• Check the project details
Nice to have
Should not have

```html
<!DOCTYPE html>
<html lang="en">
<head>
<meta charset="utf-8">
<title>Quarvin – Car Rental Dubai</title>
<link href="https://fonts.googleapis.com/css2?family=Courier+Prime:wght@400;700&display=swap" rel="stylesheet">
<style>
:root{
  --red:#c4143f;
  --red-dark:#8e0b2c;
  --ink:#1c1c1c;
  --night:#14161d;
  --white:#ffffff;
  --field:#f4f4f4;
  --panel:rgba(10,10,14,.88);
}
*{box-sizing:border-box;margin:0;padding:0}
html,body{width:839px;height:1200px;overflow:hidden;background:var(--white)}
body{position:relative;font-family:"Courier Prime","Courier New",monospace;color:var(--ink)}
.abs{position:absolute}

/* hero */
.hero{left:0;top:0;width:839px;height:410px;
  background:linear-gradient(180deg,#2a3040 0%,#6a4a3e 28%,#c9783d 44%,#4a3330 56%,#1a1a22 70%,#12131a 100%)}
.topbar{left:0;top:0;width:839px;height:78px}
.brand{left:48px;top:16px;display:flex;align-items:center;gap:10px;color:var(--white);font-weight:700;font-size:24px}
.brand-mark{width:34px;height:34px;background:var(--red)}
.top-contact{right:48px;top:10px;display:flex;align-items:center;gap:8px;color:var(--white);font-size:11px}
.dot{width:14px;height:14px;border-radius:50%;background:var(--white);opacity:.9}
.nav{right:48px;top:44px;display:flex;gap:6px}
.nav a{color:var(--white);text-decoration:none;font-size:12px;padding:4px 9px;border-radius:3px}
.nav a.active{background:var(--red)}
.hero-title{left:0;top:118px;width:839px;text-align:center;color:var(--red);font-weight:700;font-size:40px;text-shadow:0 2px 4px rgba(0,0,0,.5)}
.hero-sub{left:0;top:166px;width:839px;text-align:center;color:#eee;font-size:13px}

/* booking (children positioned inside the panel) */
.booking{left:0;top:238px;width:839px;height:172px;background:var(--panel)}
.field-label{color:var(--white);font-weight:700;font-size:11px}
.field{height:18px;background:var(--field);border-radius:2px;font-size:9px;color:#555;padding:3px 6px}
.icon{width:14px;height:14px}
.btn{display:flex;align-items:center;justify-content:center;font-size:11px;font-weight:700;color:var(--white);border-radius:3px}
.btn-quote{background:var(--red);gap:10px}
.btn-world{background:#2b2b2b;border:1px solid #555}

/* welcome */
.section-title{color:var(--red);font-weight:700;font-size:20px}
.welcome-text{left:48px;top:472px;width:330px;font-size:10px;line-height:1.4;color:#444}
.read-more{width:100px;height:26px;background:var(--red);color:var(--white);font-size:11px;border-radius:13px;display:flex;align-items:center;justify-content:center}
.car-photo{left:470px;top:450px;width:310px;height:170px;border-radius:38% 42% 14% 14%/46% 50% 16% 16%;
  background:linear-gradient(180deg,#3a3a3a 0%,#161616 45%,#0c0c0c 100%)}

/* mission */
.mission-title{left:0;top:678px;width:839px;text-align:center}
.mission-band{left:0;top:712px;width:839px;height:232px;
  background:linear-gradient(135deg,var(--red-dark) 0%,var(--red) 50%,#d9506f 100%)}
.mission-text{left:150px;top:790px;width:540px;text-align:center;color:var(--white);font-size:13px;line-height:1.45}

/* follow */
.follow-title{left:0;top:958px;width:839px;text-align:center;color:var(--red);font-weight:700;font-size:22px}
.socials{left:0;top:1000px;width:839px;display:flex;justify-content:center;gap:12px}
.social{width:36px;height:36px;border-radius:50%;background:var(--red)}

/* footer */
.footer{left:0;top:1070px;width:839px;height:100px;background:var(--night)}
.foot-col{top:1088px;width:200px;text-align:center;color:#ccc;font-size:10px}
.foot-col svg{display:block;margin:0 auto 8px}
.bottom-bar{left:0;top:1170px;width:839px;height:30px;background:var(--red);color:var(--white);font-size:9px;display:flex;align-items:center;justify-content:space-between;padding:0 48px}
</style>
</head>
<body>

<section class="hero abs" role="img" aria-label="Dusk city skyline with a silver family hatchback parked in the foreground"></section>

<header class="topbar abs">
  <div class="brand abs"><span class="brand-mark"></span>Quarvin</div>
  <div class="top-contact abs">
    <svg class="icon" viewBox="0 0 16 16"><path d="M4 1l3 3-2 2c1 2 3 4 5 5l2-2 3 3-2 3C7 15 1 9 1 3z" fill="#fff"/></svg>
    +971 4 555 0182
    <span class="dot"></span><span class="dot"></span><span class="dot"></span><span class="dot"></span>
  </div>
  <nav class="nav abs">
    <a class="active">Home</a><a>About us</a><a>Our Team</a><a>Strategy</a><a>Contact Us</a>
  </nav>
</header>

<h1 class="hero-title abs">Experience An Extra Mile</h1>
<p class="hero-sub abs">Of Comfort,Pleasure And Leisure From The Best</p>

<section class="booking abs">
  <div class="field-label abs" style="left:48px;top:18px">Pick up Location</div>
  <div class="field abs" style="left:48px;top:34px;width:262px">Select</div>
  <svg class="icon abs" style="left:316px;top:16px" viewBox="0 0 16 16"><path d="M8 1a5 5 0 0 1 5 5c0 4-5 9-5 9S3 10 3 6a5 5 0 0 1 5-5z" fill="#fff"/><circle cx="8" cy="6" r="2" fill="#222"/></svg>

  <div class="field-label abs" style="left:48px;top:62px">Pick up Date &amp; Time</div>
  <div class="field abs" style="left:48px;top:78px;width:130px"></div>
  <div class="field abs" style="left:184px;top:78px;width:60px">00</div>
  <div class="field abs" style="left:250px;top:78px;width:60px">00</div>
  <svg class="icon abs" style="left:316px;top:60px" viewBox="0 0 16 16"><circle cx="8" cy="8" r="6.5" fill="none" stroke="#fff" stroke-width="1.5"/><path d="M8 4v4l3 2" stroke="#fff" stroke-width="1.5" fill="none"/></svg>

  <div class="field-label abs" style="left:48px;top:106px">Vehicle Type</div>
  <div class="field abs" style="left:48px;top:122px;width:130px">Show All Vehicles</div>

  <div class="field-label abs" style="left:355px;top:18px">Return Location</div>
  <div class="field abs" style="left:355px;top:34px;width:262px">Select</div>
  <svg class="icon abs" style="left:623px;top:16px" viewBox="0 0 16 16"><path d="M8 1a5 5 0 0 1 5 5c0 4-5 9-5 9S3 10 3 6a5 5 0 0 1 5-5z" fill="#fff"/><circle cx="8" cy="6" r="2" fill="#222"/></svg>

  <div class="field-label abs" style="left:355px;top:62px">Return Date &amp; Time</div>
  <div class="field abs" style="left:355px;top:78px;width:130px"></div>
  <div class="field abs" style="left:491px;top:78px;width:60px">00</div>
  <div class="field abs" style="left:557px;top:78px;width:60px">00</div>
  <svg class="icon abs" style="left:623px;top:60px" viewBox="0 0 16 16"><circle cx="8" cy="8" r="6.5" fill="none" stroke="#fff" stroke-width="1.5"/><path d="M8 4v4l3 2" stroke="#fff" stroke-width="1.5" fill="none"/></svg>

  <div class="btn btn-quote abs" style="left:355px;top:120px;width:120px;height:26px">GET A QUOTE
    <svg width="12" height="10" viewBox="0 0 12 10"><path d="M0 5h10M6 1l4 4-4 4" stroke="#fff" stroke-width="1.6" fill="none"/></svg>
  </div>
  <div class="btn btn-world abs" style="left:485px;top:120px;width:132px;height:26px">Worldwide booking</div>
</section>

<h2 class="section-title abs" style="left:48px;top:440px">WELCOME TO QUARVIN</h2>
<p class="welcome-text abs">As Dubai welcomes millions of tourists and visitors each year, the local car rental industry is expected to grow more rapidly in the region.</p>
<div class="read-more abs" style="left:48px;top:530px">Read more</div>
<div class="car-photo abs" role="img" aria-label="Black sedan shown from the front three-quarter angle"></div>

<h2 class="section-title mission-title abs">MISSION &amp; VISION</h2>
<section class="mission-band abs" role="img" aria-label="Car interior photo tinted in crimson"></section>
<p class="mission-text abs">To be one of the leading auto leasing company in the fast growing economy and tourism industry of the emirate of Dubai and play alongside...</p>
<div class="read-more abs" style="left:370px;top:880px;background:#6d0820">Read more</div>

<h2 class="follow-title abs">FOLLOW US</h2>
<div class="socials abs">
  <span class="social"></span><span class="social"></span><span class="social"></span><span class="social"></span><span class="social"></span>
</div>

<footer class="footer abs"></footer>
<div class="foot-col abs" style="left:20px">
  <svg width="16" height="16" viewBox="0 0 16 16"><path d="M8 1a5 5 0 0 1 5 5c0 4-5 9-5 9S3 10 3 6a5 5 0 0 1 5-5z" fill="#fff"/><circle cx="8" cy="6" r="2" fill="#14161d"/></svg>
  P.O. Box 40417 Dubai, UAE
</div>
<div class="foot-col abs" style="left:220px">
  <svg width="16" height="16" viewBox="0 0 16 16"><path d="M4 1l3 3-2 2c1 2 3 4 5 5l2-2 3 3-2 3C7 15 1 9 1 3z" fill="#fff"/></svg>
  +971 4 555 0182
</div>
<div class="foot-col abs" style="left:420px">
  <svg width="16" height="16" viewBox="0 0 16 16"><rect x="2" y="5" width="12" height="8" fill="#fff"/><rect x="4" y="1" width="8" height="5" fill="none" stroke="#fff"/></svg>
  +971 4 555 0190
</div>
<div class="foot-col abs" style="left:620px">
  <svg width="16" height="16" viewBox="0 0 16 16"><rect x="1" y="3" width="14" height="10" fill="#fff"/><path d="M1 3l7 6 7-6" stroke="#14161d" fill="none"/></svg>
  info@quarvin-drive.example
</div>

<div class="bottom-bar abs">
  <span>Home | About Us | Our Team | Strategy | Contact Us</span>
  <span>Copyright 2015 Quarvin. All rights reserved</span>
</div>

</body>
</html>
```